*Business Card Concept For Gum (Pollution) Removal Company*
Pave Pals
*Business Card Concept For Gum (Pollution) Removal Company* - Cleaning
Creative Brief
Bright & Fun-filled
Rutger Ashdown
President
582 Willow Crest Ave. Suite K Chesapeake, Virginia 23317
1-800-615-PAVPALS (7287)
555-419-3068 Direct
info@pave-pals.example
www.pave-pals.example
Thank you for considering this project. This business card will represent my company that specializes in gum pollution removal. The next time you go to a busy shopping center or high traffic area, you might notice several unsightly black dots on the pavement. Typically they are near waste baskets. My company has a solution to removal such pollution. When designing the card I would like to include a visual element including "sticky" bubble gum and possibly variation of black dots on the pavement. If you are unclear about the "black dots", please google "chewing gum black dots". Thank you!

```html
<!DOCTYPE html>
<html lang="en">
<head>
<meta charset="utf-8">
<title>Pave Pals – Business Card</title>
<link rel="stylesheet" href="https://fonts.googleapis.com/css2?family=Poppins:wght@400;500;700;800&display=swap">
<style>
  :root {
    --pink: #ec1a8c;
    --pink-light: #f45aaf;
    --pink-deep: #d10f7a;
    --ink: #1a1a1a;
    --grey: #777777;
    --paper: #ffffff;
    --stage: #e4e4e6;
  }
  * { box-sizing: border-box; margin: 0; padding: 0; }
  html, body { width: 1200px; height: 837px; overflow: hidden; }
  body {
    background: var(--stage);
    font-family: "Poppins", sans-serif;
    position: relative;
  }
  .card {
    position: absolute;
    width: 620px;
    height: 354px;
    box-shadow: 0 8px 24px rgba(0,0,0,0.18);
    overflow: hidden;
  }
  /* Front */
  .card-front {
    left: 290px;
    top: 42px;
    background: radial-gradient(circle at 55% 40%, var(--pink-light) 0%, var(--pink) 55%, var(--pink-deep) 100%);
    color: var(--paper);
  }
  .front-brand {
    position: absolute;
    left: 46px;
    top: 58px;
  }
  .brand-name {
    font-weight: 800;
    font-size: 40px;
    line-height: 0.95;
    letter-spacing: 1px;
    text-transform: uppercase;
    width: 180px;
  }
  .brand-tagline {
    margin-top: 10px;
    font-size: 11px;
    font-weight: 500;
    white-space: nowrap;
  }
  .front-figure {
    position: absolute;
    right: 30px;
    bottom: 40px;
    width: 150px;
    height: 170px;
    border-radius: 12px;
    background: linear-gradient(180deg, rgba(255,255,255,0.35), rgba(255,255,255,0.15));
  }
  /* Back */
  .card-back {
    left: 290px;
    top: 440px;
    background: var(--paper);
    display: flex;
  }
  .back-strip {
    position: relative;
    flex: none;
    width: 200px;
    height: 100%;
    background: radial-gradient(circle at 50% 35%, var(--pink-light) 0%, var(--pink) 60%, var(--pink-deep) 100%);
    border-right: 6px solid var(--ink);
    display: flex;
    flex-direction: column;
    align-items: center;
    padding-top: 40px;
  }
  .strip-notch {
    position: absolute;
    right: -20px;
    top: 42px;
    width: 0; height: 0;
    border-top: 14px solid transparent;
    border-bottom: 14px solid transparent;
    border-left: 14px solid var(--ink);
  }
  .strip-figure {
    width: 110px;
    height: 110px;
    border-radius: 10px;
    background: rgba(255,255,255,0.3);
  }
  .strip-name {
    margin-top: 12px;
    font-weight: 800;
    font-size: 24px;
    color: var(--paper);
    text-transform: uppercase;
    letter-spacing: 1px;
    white-space: nowrap;
  }
  .back-info {
    padding: 46px 0 0 38px;
    color: var(--ink);
  }
  .person-name {
    color: var(--pink);
    font-weight: 700;
    font-size: 16px;
  }
  .person-title {
    color: var(--grey);
    font-size: 11px;
    margin-top: 2px;
  }
  .contact-list {
    list-style: none;
    margin-top: 56px;
    font-size: 10.5px;
    line-height: 1.55;
  }
  .contact-list li {
    display: flex;
    align-items: flex-start;
    gap: 10px;
  }
  .contact-icon {
    flex: none;
    width: 12px;
    height: 12px;
    margin-top: 2px;
  }
</style>
</head>
<body>
  <section class="card card-front">
    <div class="front-brand">
      <div class="brand-name">Pave Pals</div>
      <div class="brand-tagline">Sidewalk Rescue Specialist</div>
    </div>
    <div class="front-figure" role="img" aria-label="Illustration of a worker cleaning pavement with a long-handled tool"></div>
  </section>

  <section class="card card-back">
    <div class="back-strip">
      <span class="strip-notch"></span>
      <div class="strip-figure" role="img" aria-label="Illustration of a worker cleaning pavement"></div>
      <div class="strip-name">Pave Pals</div>
    </div>
    <div class="back-info">
      <div class="person-name">Rutger Ashdown</div>
      <div class="person-title">President</div>
      <ul class="contact-list">
        <li>
          <svg class="contact-icon" viewBox="0 0 12 12"><circle cx="6" cy="6" r="6" fill="var(--pink)"/><path d="M6 2.6a2.2 2.2 0 0 0-2.2 2.2C3.8 6.6 6 9.4 6 9.4s2.2-2.8 2.2-4.6A2.2 2.2 0 0 0 6 2.6z" fill="#fff"/></svg>
          <span>582 Willow Crest Ave. Suite K<br>Cedar Bay, Northfield 40117</span>
        </li>
        <li>
          <svg class="contact-icon" viewBox="0 0 12 12"><circle cx="6" cy="6" r="6" fill="var(--pink)"/><path d="M4 3l1.2 1.6-.6.8c.5.9 1.1 1.5 2 2l.8-.6L9 8l-.6.9C6 8.8 3.2 6 3.1 3.6z" fill="#fff"/></svg>
          <span>1-800-615-PAVPALS (7287)</span>
        </li>
        <li>
          <svg class="contact-icon" viewBox="0 0 12 12"><circle cx="6" cy="6" r="6" fill="var(--pink)"/><path d="M4 3l1.2 1.6-.6.8c.5.9 1.1 1.5 2 2l.8-.6L9 8l-.6.9C6 8.8 3.2 6 3.1 3.6z" fill="#fff"/></svg>
          <span>555-419-3068 Direct</span>
        </li>
        <li>
          <svg class="contact-icon" viewBox="0 0 12 12"><circle cx="6" cy="6" r="6" fill="var(--pink)"/><rect x="3" y="4" width="6" height="4.2" fill="#fff"/><path d="M3 4l3 2.4L9 4" fill="none" stroke="var(--pink)" stroke-width=".7"/></svg>
          <span>info@pave-pals.example</span>
        </li>
        <li>
          <svg class="contact-icon" viewBox="0 0 12 12"><circle cx="6" cy="6" r="6" fill="var(--pink)"/><circle cx="6" cy="6" r="3" fill="none" stroke="#fff" stroke-width=".8"/><path d="M3 6h6M6 3c-1.4 1.6-1.4 4.4 0 6M6 3c1.4 1.6 1.4 4.4 0 6" fill="none" stroke="#fff" stroke-width=".6"/></svg>
          <span>www.pave-pals.example</span>
        </li>
      </ul>
    </div>
  </section>
</body>
</html>
```